Bramblecrest Wellness Web Page

To create a web page that has the number 1 goal of converting Google Ad / Facebook Ads clicks into paying customers.
The site will feed into a web application where travellers can enter their trip and purchase a Roamwell Kit Guide.
The page / site needs to be able to tell people what we do and encourage them to start the process of getting a Roamwell Kit Guide.
It should be a wordpress theme.
Please see the attached brief for more information.

```html
<!DOCTYPE html>
<html lang="en">
<head>
<meta charset="utf-8">
<title>Bramblecrest Wellness</title>
<link rel="stylesheet" href="https://fonts.googleapis.com/css2?family=Roboto:wght@400;500;700&display=swap">
<style>
:root{
  --navy:#172b55;
  --ink:#1f2f57;
  --text:#3d4251;
  --sky:#4fa9de;
  --sky-soft:#6bb8e4;
  --panel:#eef1f9;
  --grey:#f2f2f2;
  --teal:#0f4c4f;
  --white:#ffffff;
  --black:#000000;
}
*{box-sizing:border-box;margin:0;padding:0}
html,body{width:1200px;height:4717px;overflow:hidden}
body{position:relative;font-family:"Roboto",sans-serif;color:var(--text);background:var(--white)}
.abs{position:absolute}
.btn{position:absolute;display:flex;align-items:center;justify-content:center;background:var(--navy);color:var(--white);font-weight:700;font-size:17px;letter-spacing:.3px;border-radius:22px;box-shadow:0 0 0 3px #ffffff,0 0 0 5px var(--sky)}
.heading{position:absolute;font-weight:700;color:var(--ink);font-size:30px;letter-spacing:.4px;text-transform:uppercase}
.para{position:absolute;font-size:20px;line-height:35px;color:var(--text)}
.photo{position:absolute}

/* hero */
.hero{position:absolute;left:0;top:0;width:1200px;height:597px;background:linear-gradient(180deg,#9ab3c9 0%,#e7d1b8 45%,#c9a98b 62%,#4c3a32 100%)}
.nav a{position:absolute;top:72px;font-size:17px;font-weight:500;color:var(--navy);text-decoration:none;letter-spacing:.3px}
.brand-badge{position:absolute;left:521px;top:0;width:158px;height:158px;border-radius:50%;background:var(--white);display:flex;flex-direction:column;align-items:center;justify-content:center;text-align:center}
.brand-badge span{font-size:17px;font-weight:700;color:var(--navy);line-height:21px}
.trip-form{position:absolute;left:753px;top:143px;width:335px;height:348px;background:var(--sky-soft);border-radius:14px}
.trip-form .field{position:absolute;left:35px;width:265px;height:45px;border:1.5px solid #e8f4fb;font-size:15px;color:#f4f9fc;padding:12px 14px}

/* tabs */
.tab{position:absolute;top:1242px;width:300px;height:99px;border-radius:4px;overflow:hidden;display:flex;align-items:center}
.tab .mark{width:115px;height:99px;background:#1b2a4e;display:flex;align-items:center;justify-content:center}
.tab .mark i{display:block;width:62px;height:62px;border-radius:50%;background:#e9eef6}
.tab .label{flex:1;height:99px;display:flex;align-items:center;justify-content:center;color:var(--white);font-size:26px;font-weight:700}

/* cards */
.card{position:absolute;top:2105px;width:312px;height:443px;background:var(--white);border-radius:6px;box-shadow:0 3px 10px rgba(0,0,0,.12);overflow:hidden}
.card .pic{position:absolute;left:0;top:0;width:312px;height:176px}
.card .days{position:absolute;left:33px;top:158px;width:246px;height:36px;background:var(--sky-soft);color:var(--white);font-size:14px;font-weight:700;display:flex;align-items:center;padding-left:52px}
.card .days svg{position:absolute;left:18px;top:8px}
.card .title{position:absolute;left:34px;top:220px;font-size:21px;font-weight:700;color:var(--ink)}
.card .place{position:absolute;left:74px;top:268px;font-size:20px;color:var(--text)}
.card .pin{position:absolute;left:34px;top:263px}
.card .blurb{position:absolute;left:21px;top:310px;font-size:20px;color:var(--text);white-space:nowrap}
.card .btn{left:12px;top:383px;width:168px;height:38px;font-size:16px;box-shadow:none}
.card .from{position:absolute;right:18px;top:378px;text-align:right;font-weight:700;color:var(--ink);font-size:20px;line-height:37px}

/* what is in */
.inside{position:absolute;left:0;top:2686px;width:1200px;height:619px;background:linear-gradient(90deg,#1b4a2d 0%,#24563a 40%,#0f5658 62%,#0c4f57 100%)}
.checks li{list-style:none;position:absolute;right:655px;color:var(--white);font-size:20px;white-space:nowrap}
.checks svg{position:absolute;left:-36px;top:2px}

/* search */
.finder{position:absolute;left:112px;top:3550px;width:976px;height:140px;background:var(--white);border-radius:4px;box-shadow:0 2px 8px rgba(0,0,0,.1)}
.finder .col{position:absolute;top:0;height:140px}
.finder h4{position:absolute;font-size:20px;font-weight:500;color:var(--ink);top:44px;white-space:nowrap}
.finder p{position:absolute;font-size:18px;color:var(--text);top:84px;white-space:nowrap}
.finder .sep{position:absolute;top:10px;width:1px;height:120px;background:#dde1ea}

.malaria-item{position:absolute;font-size:21px;color:var(--text)}
.ring{position:absolute;width:88px;height:88px;border-radius:50%;background:var(--sky);box-shadow:0 0 0 4px #ffffff,0 0 0 6px var(--sky)}

/* footer */
.footer{position:absolute;left:0;top:4397px;width:1200px;height:320px;background:var(--black);color:var(--white)}
.footer nav a{position:absolute;top:172px;font-size:17px;font-weight:700;color:var(--white);text-decoration:none}
.social{position:absolute;top:211px;width:28px;height:28px;border-radius:50%}
</style>
</head>
<body>

<!-- HERO -->
<header class="hero" role="img" aria-label="Photo of a traveller with a backpack and hat raising arms on a beach at sunset, cliffs on the left"></header>
<nav class="nav">
  <a class="abs" style="left:283px">HOME</a>
  <a class="abs" style="left:372px">ABOUT US</a>
  <a class="abs" style="left:740px">DISEASE</a>
  <a class="abs" style="left:843px">COUNTRY</a>
</nav>
<div class="brand-badge"><span>Bramblecrest<br>Wellness</span></div>
<form class="trip-form">
  <div class="field" style="top:45px">Name</div>
  <div class="field" style="top:114px">Type of Trip</div>
  <div class="field" style="top:183px">Price</div>
  <div class="btn" style="left:82px;top:270px;width:172px;height:40px;font-size:16px;box-shadow:none">PURCHASE</div>
</form>

<!-- ABOUT -->
<div class="photo" style="left:0;top:683px;width:605px;height:391px;border-radius:0 380px 380px 0/0 200px 200px 0;background:linear-gradient(180deg,#7b88a6 0%,#e6a57c 45%,#f2b56a 55%,#3d3a44 100%);box-shadow:4px 0 0 var(--navy)" role="img" aria-label="Photo of a boat bow facing a sunset over karst islands"></div>
<h2 class="heading" style="left:632px;top:695px">What is Bramblecrest Wellness?</h2>
<p class="para" style="left:632px;top:748px;width:470px">Sed ut perspiciatis unde omnis iste natus error sit voluptatem accusantium doloremque laudantium, totam rem aperiam, eaque ipsa quae ab illo inventore veritatis et quasi architecto beatae vitae dicta sunt explicabo. Nemo enim ipsam voluptatem quia voluptas sit aspernatur aut odit aut fugit, sed quia consequuntur magni dolores</p>
<div class="btn" style="left:632px;top:1022px;width:170px;height:40px">READ MORE</div>

<!-- EXAMPLE -->
<h2 class="heading" style="left:0;width:1200px;text-align:center;top:1157px">Example of a Roamwell Kit Guide</h2>
<div class="tab" style="left:115px"><div class="mark"><i style="background:#2f6fb8"></i></div><div class="label" role="img" aria-label="Photo of white houses on a Greek island" style="background:linear-gradient(90deg,#3d5f8c,#6f95be)">GREECE</div></div>
<div class="tab" style="left:452px;overflow:visible"><div class="mark" style="background:var(--sky-soft)"><i style="background:#e9eef6"></i></div><div class="label" role="img" aria-label="Photo of the Paris skyline" style="background:linear-gradient(90deg,#7fa6c9,#a68f6a)">FRANCE</div>
  <svg class="abs" style="left:140px;top:99px" width="22" height="12"><path d="M0 0H22L11 12Z" fill="#4fa9de"/></svg></div>
<div class="tab" style="left:782px"><div class="mark"><i style="background:#2d8c4a"></i></div><div class="label" role="img" aria-label="Photo of giraffes on the savanna" style="background:linear-gradient(90deg,#6e6a3a,#8a7a46)">AFRICA</div></div>

<!-- ADVENTURE -->
<h3 class="abs" style="right:638px;top:1450px;text-align:right;font-size:25px;line-height:38px;font-weight:500;color:var(--sky)">ADVENTURE &amp; EXPERIENCE<br>THE TRAVEL</h3>
<p class="para" style="left:100px;top:1538px;width:467px;text-align:right">Sed ut perspiciatis unde omnis iste natus error sit voluptatem accusantium doloremque laudantium, totam rem aperiam, eaque ipsa quae ab illo inventore veritatis et quasi architecto beatae vitae dicta sunt explicabo. Nemo enim ipsam voluptatem quia voluptas sit aspernatur aut odit aut fugit, sed quia consequuntur magni dolores eos qui ratione voluptatem sequi nesciunt.</p>
<div class="btn" style="left:429px;top:1845px;width:170px;height:39px">LEARN MORE</div>
<div class="photo" style="left:603px;top:1396px;width:231px;height:405px;border-radius:116px;background:linear-gradient(180deg,#b9cde0 0%,#7d9bb4 40%,#3a8fa8 70%,#6a7a7e 100%)" role="img" aria-label="Photo of two hikers with backpacks by a mountain lake"></div>
<div class="photo" style="left:857px;top:1447px;width:233px;height:409px;border-radius:117px;background:linear-gradient(180deg,#cfd7dc 0%,#b58b6e 45%,#9bc7d8 100%);box-shadow:0 0 0 3px var(--sky)" role="img" aria-label="Photo of two smiling travellers reading a map"></div>

<!-- WHY BUY -->
<section class="abs" style="left:0;top:1971px;width:1200px;height:715px;background:var(--panel)"></section>
<h2 class="heading" style="left:0;width:1200px;text-align:center;top:2018px">Why buy a Roamwell Kit Guide</h2>

<article class="card" style="left:112px">
  <div class="pic" role="img" aria-label="Photo of a resort pool among pine trees" style="background:linear-gradient(180deg,#c9b07a,#4f6b3c 55%,#4fb3d6)"></div>
  <div class="days"><svg width="20" height="20"><circle cx="10" cy="10" r="8" fill="none" stroke="#fff" stroke-width="2"/><path d="M10 5v5l3 2" stroke="#fff" stroke-width="2" fill="none"/></svg>5 DAYS</div>
  <div class="title">LOREM IPSUM</div>
  <svg class="pin" width="26" height="32"><path d="M13 1C6 1 1 6 1 12c0 8 12 19 12 19s12-11 12-19C25 6 20 1 13 1z" fill="#2b78d8"/><circle cx="13" cy="12" r="5" fill="#fff"/></svg>
  <div class="place">Italy</div>
  <div class="blurb">Sed ut perspiciatis unde omnis</div>
  <div class="btn">GET DETAILS</div>
  <div class="from">FROM<br>$67.9</div>
</article>
<article class="card" style="left:443px">
  <div class="pic" role="img" aria-label="Photo of a city skyline at dusk" style="background:linear-gradient(180deg,#6a7fa6,#3c4a6e 50%,#c08a52)"></div>
  <div class="days"><svg width="20" height="20"><circle cx="10" cy="10" r="8" fill="none" stroke="#fff" stroke-width="2"/><path d="M10 5v5l3 2" stroke="#fff" stroke-width="2" fill="none"/></svg>7 DAYS</div>
  <div class="title">LOREM IPSUM</div>
  <svg class="pin" width="26" height="32"><path d="M13 1C6 1 1 6 1 12c0 8 12 19 12 19s12-11 12-19C25 6 20 1 13 1z" fill="#2b78d8"/><circle cx="13" cy="12" r="5" fill="#fff"/></svg>
  <div class="place">France</div>
  <div class="blurb">Sed ut perspiciatis unde omnis</div>
  <div class="btn">GET DETAILS</div>
  <div class="from">FROM<br>$92.9</div>
</article>
<article class="card" style="left:775px">
  <div class="pic" role="img" aria-label="Photo of a red suspension bridge over a bay at sunset" style="background:linear-gradient(180deg,#e0a764,#b4553a 50%,#3a5e7a)"></div>
  <div class="days"><svg width="20" height="20"><circle cx="10" cy="10" r="8" fill="none" stroke="#fff" stroke-width="2"/><path d="M10 5v5l3 2" stroke="#fff" stroke-width="2" fill="none"/></svg>15 DAYS</div>
  <div class="title">LOREM IPSUM</div>
  <svg class="pin" width="26" height="32"><path d="M13 1C6 1 1 6 1 12c0 8 12 19 12 19s12-11 12-19C25 6 20 1 13 1z" fill="#2b78d8"/><circle cx="13" cy="12" r="5" fill="#fff"/></svg>
  <div class="place">California</div>
  <div class="blurb">Sed ut perspiciatis unde omnis</div>
  <div class="btn">GET DETAILS</div>
  <div class="from">FROM<br>$105.92</div>
</article>
<div class="btn" style="left:515px;top:2600px;width:170px;height:38px;box-shadow:none;font-size:16px">BUY NOW TRIPS</div>

<!-- WHAT IS IN -->
<section class="inside" role="img" aria-label="Aerial photo of tropical forest meeting the sea"></section>
<h2 class="abs" style="right:654px;top:2812px;text-align:right;font-size:30px;line-height:38px;font-weight:700;color:var(--white)">WHAT IS IN A ROAMWELL<br>KIT GUIDE</h2>
<p class="abs" style="right:650px;top:2905px;width:470px;text-align:right;font-size:20px;line-height:35px;color:var(--white)">Sed ut perspiciatis unde omnis iste natus error sit voluptatem accusantium doloremque laudantium,</p>
<ul class="checks">
  <li style="top:3002px"><svg width="22" height="20"><path d="M3 10l6 6L20 3" stroke="#fff" stroke-width="3" fill="none"/></svg>Lorem ipsum dolor sit ame</li>
  <li style="top:3046px"><svg width="22" height="20"><path d="M3 10l6 6L20 3" stroke="#fff" stroke-width="3" fill="none"/></svg>Lorem ipsum dolor sit ame</li>
  <li style="top:3089px"><svg width="22" height="20"><path d="M3 10l6 6L20 3" stroke="#fff" stroke-width="3" fill="none"/></svg>Lorem ipsum dolor sit ame</li>
</ul>
<div class="btn" style="left:378px;top:3158px;width:170px;height:38px;font-size:16px;box-shadow:0 0 0 2px #ffffff">SEE ALL SERVICES</div>
<div class="photo" style="left:595px;top:2730px;width:499px;height:540px;border:5px solid var(--white);background:linear-gradient(180deg,#5aa3d6 0%,#8cc4e6 25%,#3c7b52 45%,#1fa7c8 65%,#8b6b4e 100%)" role="img" aria-label="Photo of a woman in a sun hat sitting on a pier facing a limestone island"></div>
<svg class="abs" style="left:610px;top:2980px" width="24" height="36"><path d="M18 4L6 18l12 14" stroke="#1b1b1b" stroke-width="4" fill="none"/></svg>
<svg class="abs" style="left:1050px;top:2980px" width="24" height="36"><path d="M6 4l12 14L6 32" stroke="#fff" stroke-width="4" fill="none"/></svg>

<!-- VACCINES -->
<section class="abs" style="left:0;top:3305px;width:1200px;height:1092px;background:var(--grey)"></section>
<h2 class="heading" style="left:0;width:1200px;text-align:center;top:3385px">What vaccines do I need for....</h2>
<p class="abs" style="left:100px;width:1000px;top:3437px;text-align:center;font-size:20px;line-height:35px">Sed ut perspiciatis unde omnis iste natus error sit voluptatem accusantium doloremque laudantium, totam rem aperiam, eaque ipsa quae ab illo inventore veritatis et quasi architecto beatae vitae dicta sunt</p>
<div class="finder">
  <svg class="abs" style="left:44px;top:40px" width="52" height="52"><circle cx="21" cy="21" r="16" fill="none" stroke="#4fa9de" stroke-width="4"/><path d="M33 33l15 15" stroke="#4fa9de" stroke-width="4"/></svg>
  <h4 style="left:115px">SEARCH</h4><p style="left:115px">Insert Keyword</p>
  <div class="sep" style="left:290px"></div>
  <svg class="abs" style="left:340px;top:36px" width="56" height="64"><path d="M28 4C18 4 11 11 11 20c0 12 17 28 17 28s17-16 17-28C45 11 38 4 28 4z" fill="none" stroke="#4fa9de" stroke-width="3.5"/><circle cx="28" cy="20" r="6" fill="none" stroke="#4fa9de" stroke-width="3.5"/><ellipse cx="28" cy="52" rx="24" ry="8" fill="none" stroke="#4fa9de" stroke-width="3"/></svg>
  <h4 style="left:422px">DESTINATIONS</h4><p style="left:422px">All Destinations <svg width="14" height="10"><path d="M2 2l5 5 5-5" stroke="#1f2f57" stroke-width="2" fill="none"/></svg></p>
  <div class="sep" style="left:634px"></div>
  <svg class="abs" style="left:700px;top:42px" width="56" height="50"><g fill="none" stroke="#4fa9de" stroke-width="3.5"><rect x="2" y="4" width="8" height="8"/><rect x="2" y="20" width="8" height="8"/><rect x="2" y="36" width="8" height="8"/><path d="M16 8h36M16 24h36M16 40h36"/></g></svg>
  <h4 style="left:772px">TYPOLOGIES</h4><p style="left:772px">All Typologies <svg width="14" height="10"><path d="M2 2l5 5 5-5" stroke="#1f2f57" stroke-width="2" fill="none"/></svg></p>
</div>
<div class="btn" style="left:515px;top:3748px;width:170px;height:39px;font-size:16px;box-shadow:none">SEARCH</div>

<h2 class="heading" style="left:0;width:1200px;text-align:center;top:3869px">What antimalarials do I need for...</h2>
<div class="photo" style="left:467px;top:3957px;width:266px;height:348px;border-radius:4px;background:linear-gradient(180deg,#4a8cc4 0%,#d2b48c 40%,#c48462 65%,#3b8fb0 100%)" role="img" aria-label="Photo of a colourful coastal village on a cliff above the sea"></div>
<span class="malaria-item" style="right:916px;top:4055px">Lorem ipsum</span>
<span class="malaria-item" style="right:916px;top:4182px">Lorem ipsum</span>
<span class="malaria-item" style="left:912px;top:4055px">Lorem ipsum</span>
<span class="malaria-item" style="left:912px;top:4182px">Lorem ipsum</span>
<div class="ring" style="left:302px;top:4025px"><svg width="88" height="88"><path d="M30 58l28-28M40 34l22 8-4 4M34 52l-4 10 10-4" stroke="#fff" stroke-width="3" fill="none"/></svg></div>
<div class="ring" style="left:302px;top:4152px"><svg width="88" height="88"><rect x="30" y="28" width="28" height="34" rx="3" fill="none" stroke="#fff" stroke-width="3"/><circle cx="44" cy="44" r="8" fill="none" stroke="#fff" stroke-width="2.5"/></svg></div>
<div class="ring" style="left:798px;top:4025px"><svg width="88" height="88"><circle cx="44" cy="44" r="18" fill="none" stroke="#fff" stroke-width="3"/><path d="M26 44h36M44 26c-8 10-8 26 0 36M44 26c8 10 8 26 0 36" stroke="#fff" stroke-width="2.5" fill="none"/></svg></div>
<div class="ring" style="left:798px;top:4152px"><svg width="88" height="88"><path d="M24 56h40M30 62h28" stroke="#fff" stroke-width="3"/><circle cx="52" cy="36" r="6" fill="none" stroke="#fff" stroke-width="2.5"/><path d="M34 56V36M34 36l-8 6M34 36l8 4" stroke="#fff" stroke-width="2.5" fill="none"/></svg></div>

<!-- FOOTER -->
<footer class="footer">
  <div class="abs" style="left:0;width:1200px;top:78px;text-align:center;font-size:22px;font-weight:700;line-height:28px">Bramblecrest<br>Wellness</div>
  <nav>
    <a style="left:403px">HOME</a>
    <a style="left:492px">ABOUT US</a>
    <a style="left:611px">DISEASE</a>
    <a style="left:714px">COUNTRY</a>
  </nav>
  <span class="social" style="left:539px;background:#3b5ba8"></span>
  <span class="social" style="left:584px;background:#2aa3e6"></span>
  <span class="social" style="left:630px;background:#d6387a"></span>
  <div class="abs" style="left:112px;top:256px;width:976px;height:1px;background:#3a3a3a"></div>
  <div class="abs" style="left:0;width:1200px;top:285px;text-align:center;font-size:15px">@2023 COPYRIGHTS. BRAMBLECREST WELLNESS. ALL RIGHTS RESERVED.</div>
</footer>

</body>
</html>
```